Brick on business card for client

Require a business card design for a new company based in Trinidad & Tobago called "Brick on".

We source building supplies for resident and commercial projects. We manage and supply all your building solutions.

Exp: If you was to build a house or commercial building, My company Brick on will supply and install all your building needs. Floor tile, Windows, Door, Molding .

Target Market(s)

Construction client

Industry/Entity Type

Building

Contact Information for Business Card

BRICK ON LIMITED
HARBOURVIEW TRADE PLAZA
LA VALLETTE, EXT. NO. 4, BLDG 3
SAN JUAN, TRINIDAD, W.I.
868-492-6031
brickonlimited-example.com
dorian@brickonlimited-example.com

Font styles to use
Serif

Requirements
Must have
• Company name
• Address
• My Name: Dorian Kowlessar
• Director
Nice to have
• Modern business card (With a new logo)

```html
<!DOCTYPE html>
<html lang="en">
<head>
<meta charset="utf-8">
<title>Brick on Limited – Business Card</title>
<link rel="stylesheet" href="https://fonts.googleapis.com/css2?family=Crimson+Text:wght@400;700&display=swap">
<style>
  :root {
    --backdrop: #2a2a2c;
    --card: #ffffff;
    --gold: #e2b77a;
    --silver: #a7b0b9;
    --ink: #1d1d1d;
    --ink-soft: #3a3a3a;
  }
  * { margin: 0; padding: 0; box-sizing: border-box; }
  html, body { width: 1200px; height: 852px; overflow: hidden; }
  body {
    background: var(--backdrop);
    font-family: "Crimson Text", serif;
    color: var(--ink);
    position: relative;
  }
  .card {
    position: absolute;
    width: 540px;
    height: 309px;
    background: var(--card);
    border-radius: 12px;
    overflow: hidden;
  }
  .card--front { left: 40px; top: 170px; }
  .card--back  { left: 620px; top: 370px; }

  .brand { display: flex; align-items: center; gap: 12px; }
  .brand__mark { width: 18px; height: 18px; background: var(--gold); flex: none; }
  .brand__name {
    font-size: 38px; font-weight: 700; color: var(--ink);
    letter-spacing: 0.5px; line-height: 1;
  }
  .brand__tagline { font-size: 16px; color: var(--ink); margin-top: 6px; margin-left: 30px; }

  .card--front .brand-block { position: absolute; left: 112px; top: 116px; }

  .card__art { position: absolute; inset: 0; }

  .holder { position: absolute; right: 26px; top: 22px; text-align: right; }
  .holder__name { font-size: 23px; font-weight: 700; line-height: 1.1; }
  .holder__title { font-size: 15px; color: var(--ink-soft); }

  .card--back .brand-block { position: absolute; left: 36px; top: 90px; }
  .card--back .brand__name { font-size: 30px; }
  .card--back .brand__mark { width: 14px; height: 14px; }
  .card--back .brand__tagline { font-size: 13px; margin-left: 26px; margin-top: 4px; }

  .address { position: absolute; left: 36px; top: 168px; }
  .address__site { font-size: 17px; letter-spacing: 0.3px; margin-bottom: 4px; }
  .address__lines { display: flex; gap: 6px; font-size: 14px; line-height: 1.3; color: var(--ink-soft); }
  .address__lines svg { flex: none; margin-top: 3px; }

  .contact { position: absolute; right: 22px; top: 140px; list-style: none; text-align: right; }
  .contact li {
    display: flex; justify-content: flex-end; align-items: center; gap: 8px;
    font-size: 15px; line-height: 1.65; color: var(--ink);
  }
  .contact svg { flex: none; }
</style>
</head>
<body>

<section class="card card--front" aria-label="Card front">
  <div class="brand-block">
    <div class="brand">
      <span class="brand__mark"></span>
      <span class="brand__name">BRICK ON LIMITED</span>
    </div>
    <p class="brand__tagline">For All Your Building Solutions...</p>
  </div>
</section>

<section class="card card--back" aria-label="Card back">
  <svg class="card__art" viewBox="0 0 540 309" width="540" height="309" aria-hidden="true">
    <path d="M540 86 C440 110 420 225 320 262 C240 292 110 280 0 290 L0 309 L540 309 Z" fill="var(--gold)"/>
    <path d="M540 62 C430 92 410 215 310 252 C230 284 110 270 0 276" fill="none" stroke="var(--silver)" stroke-width="11"/>
    <path d="M520 58 C410 102 400 200 300 240 C240 264 160 268 80 266" fill="none" stroke="var(--silver)" stroke-width="4" opacity="0.7"/>
  </svg>

  <div class="holder">
    <p class="holder__name">Dorian Kowlessar</p>
    <p class="holder__title">Director</p>
  </div>

  <div class="brand-block">
    <div class="brand">
      <span class="brand__mark"></span>
      <span class="brand__name">BRICK ON LIMITED</span>
    </div>
    <p class="brand__tagline">For All Your Building Solutions...</p>
  </div>

  <div class="address">
    <p class="address__site">HARBOURVIEW TRADE PLAZA</p>
    <div class="address__lines">
      <svg width="10" height="14" viewBox="0 0 10 14"><path d="M5 0a5 5 0 0 1 5 5c0 3.5-5 9-5 9S0 8.5 0 5a5 5 0 0 1 5-5z" fill="var(--ink)"/><circle cx="5" cy="5" r="2" fill="#fff"/></svg>
      <p>La Vallette, Ext. No. 4 Bldg 3<br>San Juan, Trinidad, W.I.</p>
    </div>
  </div>

  <ul class="contact">
    <li>868-492-6031
      <svg width="13" height="12" viewBox="0 0 13 12"><path d="M1 4c0-2 2-3 5.5-3S12 2 12 4l-2.5 1-1-1.5h-4l-1 1.5z M3 6h7l1 5H2z" fill="var(--ink)"/></svg>
    </li>
    <li>brickonlimited-example.com
      <svg width="12" height="12" viewBox="0 0 12 12"><circle cx="6" cy="6" r="5.2" fill="none" stroke="var(--ink)" stroke-width="1.2"/><path d="M0.8 6h10.4M6 0.8v10.4" stroke="var(--ink)" stroke-width="1"/><ellipse cx="6" cy="6" rx="2.4" ry="5.2" fill="none" stroke="var(--ink)" stroke-width="1"/></svg>
    </li>
    <li>dorian@brickonlimited-example.com
      <svg width="13" height="10" viewBox="0 0 13 10"><rect x="0.5" y="0.5" width="12" height="9" fill="var(--ink)"/><path d="M0.5 0.5l6 5 6-5" fill="none" stroke="#fff" stroke-width="1"/></svg>
    </li>
  </ul>
</section>

</body>
</html>
```